Wine label design for my wife. Wine called "The Mirabel"

I need a wine label face lift of one of my premium wines in my collection. My wine sells in Harbor Lark's all over the States. My current label is called The Mirabel (my wife's name) and the illustration of her eyes is done by a well know artist from South Africa. I do not have to use this illustration and therefor I attached several pictures of her and her eyes, even when she was a little girl. The wine's also made in South Africa. This is a premium wine that we only sell 2000 bottles per year. The wine sells at 60 usd per bottle, The current label is too white. I also think her eyes should look more at the person buying it, than away from them.

Target Market(s)

Top end wine buyers

Font styles to use
Decorative
Script

Requirements
Must have
• 'The Mirabel' must be on the label
An illustration must be on the label
Basically all the info that's on the current label must be on by law. As per Sample
Nice to have
• Maybe some ideas of her whole face?
Should not have
• any gold colour

```html
<!DOCTYPE html>
<html lang="en">
<head>
<meta charset="utf-8">
<title>The Mirabel — Sauvignon Blanc Label</title>
<link rel="stylesheet" href="https://fonts.googleapis.com/css2?family=Parisienne&family=Abel&family=Alegreya:wght@400&display=swap">
<style>
  :root {
    --label-bg: #2e2e2e;
    --outer-frame: #4f4f4f;
    --inner-rule: #650000;
    --title-ink: #cfcfcf;
    --title-shadow: #050505;
    --portrait-mat: #464646;
    --portrait-mat-shadow: #262626;
    --portrait-light: #e4e4e4;
    --portrait-mid: #a9a9a9;
    --portrait-dark: #3a3a3a;
    --accent-silver: #a8adb3;
    --plaque-line: #858585;
    --plaque-text: #cdcdcd;
    --ornament-tone: #4a4a4a;
  }
  * { box-sizing: border-box; margin: 0; padding: 0; }
  html, body {
    width: 960px; height: 1200px; overflow: hidden;
    background: var(--label-bg);
  }
  .label {
    position: relative;
    width: 960px; height: 1200px;
    background: var(--label-bg);
    border: 9px solid var(--outer-frame);
    overflow: hidden;
  }
  .label__rule {
    position: absolute;
    inset: 1px;
    border: 4px solid var(--inner-rule);
    pointer-events: none;
  }
  .vine-ornament {
    position: absolute;
    background: radial-gradient(ellipse at center, var(--ornament-tone) 0%, rgba(74,74,74,0.35) 55%, rgba(46,46,46,0) 80%);
    opacity: 0.7;
  }
  .vine-ornament--top { left: 201px; top: 3px; width: 560px; height: 240px; }
  .vine-ornament--bottom { left: 361px; top: 1056px; width: 140px; height: 125px; }

  .wine-name {
    position: absolute;
    left: 0; top: 288px; width: 942px;
    text-align: center;
    font-family: "Parisienne", cursive;
    font-weight: 400;
    color: var(--title-ink);
    text-shadow: 4px 4px 0 var(--title-shadow);
    white-space: nowrap;
    line-height: 1;
  }
  .wine-name__article { font-size: 58px; margin-right: 2px; }
  .wine-name__given { font-size: 188px; }

  .portrait {
    position: absolute;
    left: 93px; top: 557px;
    width: 766px; height: 295px;
    background: var(--portrait-mat);
    box-shadow: -8px 8px 0 var(--portrait-mat-shadow);
  }
  .portrait__art {
    position: absolute;
    left: 26px; top: 21px;
    width: 712px; height: 252px;
    background: linear-gradient(90deg, var(--portrait-light) 0%, var(--portrait-mid) 12%, var(--portrait-light) 30%, var(--portrait-light) 72%, var(--portrait-dark) 86%, var(--portrait-light) 100%);
  }

  .varietal {
    position: absolute;
    left: 0; top: 904px; width: 942px;
    text-align: center;
    font-family: "Abel", sans-serif;
    font-size: 21px;
    letter-spacing: 0.5px;
    color: var(--accent-silver);
  }

  .producer-plaque {
    position: absolute;
    left: 263px; top: 941px;
    width: 406px; height: 95px;
  }
  .producer-plaque svg { position: absolute; inset: 0; }
  .producer-plaque__name {
    position: absolute;
    left: 0; top: 17px; width: 100%;
    text-align: center;
    font-family: "Alegreya", serif;
    font-size: 30px;
    color: var(--plaque-text);
    letter-spacing: 0.3px;
  }
  .producer-plaque__vintage {
    position: absolute;
    left: 0; top: 55px; width: 100%;
    text-align: center;
    font-family: "Abel", sans-serif;
    font-size: 22px;
    color: var(--accent-silver);
  }
</style>
</head>
<body>
  <main class="label">
    <div class="label__rule"></div>

    <div class="vine-ornament vine-ornament--top" role="img" aria-label="Engraved grape vine leaves and tendrils trailing from the top edge"></div>

    <h1 class="wine-name">
      <span class="wine-name__article">The</span><span class="wine-name__given">Mirabel</span>
    </h1>

    <figure class="portrait">
      <div class="portrait__art" role="img" aria-label="Black and white pencil illustration of Mirabel's eyes and brows"></div>
    </figure>

    <p class="varietal">SAUVIGNON BLANC</p>

    <div class="producer-plaque">
      <svg width="406" height="95" viewBox="0 0 406 95" aria-hidden="true">
        <path d="M14 1 H392 V8 A6 6 0 0 0 398 14 H405 V81 H398 A6 6 0 0 0 392 87 V94 H14 V87 A6 6 0 0 0 8 81 H1 V14 H8 A6 6 0 0 0 14 8 Z"
              fill="none" stroke="var(--plaque-line)" stroke-width="1.5"/>
        <path d="M22 8 H384 V12 A10 10 0 0 0 394 22 H398 V73 H394 A10 10 0 0 0 384 83 V87 H22 V83 A10 10 0 0 0 12 73 H8 V22 H12 A10 10 0 0 0 22 12 Z"
              fill="none" stroke="var(--plaque-line)" stroke-width="1.5"/>
      </svg>
      <p class="producer-plaque__name">ASHFORD VALE WINES</p>
      <p class="producer-plaque__vintage">2017</p>
    </div>

    <div class="vine-ornament vine-ornament--bottom" role="img" aria-label="Faint engraved vine leaf at the bottom edge"></div>
  </main>
</body>
</html>
```